Silver Heron Holdings, LLC Business Card

We need a logo that will be embossed or printed in a singular light color for Business Cards. Would be interested in seeing a Cypress Tree graphic. Our company name is Silver Heron Holdings, LLC. Business Card layout and graphic should project imagine of confidence, integrity and strength.

```html
<!DOCTYPE html>
<html lang="en">
<head>
<meta charset="utf-8">
<title>Silver Heron Holdings, LLC – Business Card</title>
<link rel="stylesheet" href="https://fonts.googleapis.com/css2?family=Questrial&display=swap">
<style>
  :root {
    --backdrop: #e9e6e0;
    --card-dark: #373737;
    --card-light: #f4f4f4;
    --ink-light: #ffffff;
    --ink-dark: #3a3a3a;
    --ink-muted: #555555;
    --shadow: rgba(0, 0, 0, 0.18);
  }
  * { box-sizing: border-box; margin: 0; padding: 0; }
  html, body {
    width: 1200px;
    height: 800px;
    overflow: hidden;
    background: var(--backdrop);
    font-family: "Questrial", "Century Gothic", sans-serif;
  }
  .canvas {
    position: relative;
    width: 1200px;
    height: 800px;
  }
  .card {
    position: absolute;
    box-shadow: 0 6px 18px var(--shadow);
  }
  .card-front {
    left: 170px;
    top: 230px;
    width: 560px;
    height: 300px;
    background: var(--card-dark);
    display: flex;
    align-items: center;
    justify-content: center;
  }
  .card-back {
    left: 470px;
    top: 420px;
    width: 600px;
    height: 300px;
    background: var(--card-light);
    color: var(--ink-dark);
  }
  .company-name {
    font-size: 25px;
    letter-spacing: 0.06em;
    text-transform: uppercase;
    white-space: nowrap;
  }
  .card-front .company-name { color: var(--ink-light); }
  .card-back .company-name {
    position: absolute;
    right: 46px;
    top: 56px;
    font-size: 21px;
    color: var(--ink-dark);
  }
  .contact {
    position: absolute;
    left: 44px;
    bottom: 36px;
    font-size: 12.5px;
    line-height: 1.45;
    color: var(--ink-muted);
  }
  .contact .label { font-weight: bold; color: var(--ink-dark); }
  .holder {
    position: absolute;
    right: 46px;
    bottom: 36px;
    text-align: right;
    line-height: 1.3;
  }
  .holder-name {
    font-size: 15px;
    font-weight: bold;
    color: var(--ink-dark);
  }
  .holder-title {
    font-size: 12.5px;
    color: var(--ink-muted);
  }
</style>
</head>
<body>
  <main class="canvas">
    <section class="card card-front" aria-label="Business card front">
      <p class="company-name">Silver Heron Holdings, LLC</p>
    </section>

    <section class="card card-back" aria-label="Business card back">
      <p class="company-name">Silver Heron Holdings, LLC</p>
      <div class="contact">
        <p>Lindenweg 214, CH-3012 Bern</p>
        <p><span class="label">Phone:</span> +41 31 555 01 42 · www.silverheronhold.com</p>
      </div>
      <div class="holder">
        <p class="holder-name">Helena MARSH</p>
        <p class="holder-title">Managing Partner</p>
      </div>
    </section>
  </main>
</body>
</html>
```